creative pack design with extended budget for Velmoraq coffee product

- we need a packing design for a new product of coffee for our company Tesmo Kirul located in Uganda.
- specialty Arabica coffee grown at slopes of Mountain Elgon with rich volcanic soils located in Eastern region of Uganda.
-  we have a logo already made and has registered in Uganda. our logo colors are mixture between a lot of brown color and yellow. vacuum  plastic bags.
- there is no restrictions towards your imagination .
-  all details available
- we will launch our product through phases ;
- phase 1 is  a ground coffee : ( Turkish coffee )  2 degrees of roasting which are ( medium dark , light ) of 250 grm
b) roasted beans: 2 degrees ( medium, dark) of 250 grm & 1000 grm
- we need also to highlight the eastern spirit of Turkish coffee
- we  need designs, the info and color only will be changed depending on previous classifications

Target Market(s)
Arab countries, Turkey , Uganda, Europe
Colors
Designer to choose colors to be used in the design.
Requirements
Nice to have
- about nature , Elgon mountain , farmers, freshness, distinctive product, soul of east such as decorated cup of Turkish coffee . these just an ideas but there is no restrictions on your imagination

```html
<!DOCTYPE html>
<html lang="en">
<head>
<meta charset="utf-8">
<title>Velmoraq Coffee – Roasted Beans Pack</title>
<link rel="stylesheet" href="https://fonts.googleapis.com/css2?family=Oswald:wght@400;500;600&family=Arimo:wght@400;700&display=swap">
<style>
  :root {
    --backdrop: #1c1c1c;
    --foil: #e6e6e6;
    --foil-light: #f3f3f3;
    --foil-shade: #cfcfcf;
    --ink: #222222;
    --brown: #5a3426;
    --brown-deep: #4a2a1f;
    --tan: #dcc09a;
    --copper: #b8733a;
    --copper-light: #f0b46a;
    --photo-dark: #4a4a4a;
    --photo-mid: #8c8c8c;
    --photo-light: #d2d2d2;
  }
  * { margin: 0; padding: 0; box-sizing: border-box; }
  html, body {
    width: 1200px; height: 1093px; overflow: hidden;
    background: var(--backdrop);
  }
  .canvas { position: relative; width: 1200px; height: 1093px; }

  .pack { position: absolute; left: 370px; top: 128px; width: 450px; height: 862px; }

  .pack-side {
    position: absolute; left: 0; top: 0; width: 60px; height: 100%;
    background: linear-gradient(90deg, var(--foil-shade), var(--foil) 60%, var(--foil-shade));
  }
  .pack-side__text {
    position: absolute; left: 8px; top: 250px; width: 46px;
    font: 400 8px/12px "Arimo", sans-serif; color: #555;
  }

  .pack-front {
    position: absolute; left: 60px; top: 0; width: 390px; height: 100%;
    background: var(--foil); overflow: hidden;
  }
  .seal {
    position: absolute; left: 0; top: 0; width: 100%; height: 78px;
    background: linear-gradient(180deg, var(--foil-light), var(--foil));
    display: flex; align-items: center; justify-content: center;
  }
  .seal__tagline { font: 700 22px "Arimo", sans-serif; color: var(--ink); }
  .copper-band {
    position: absolute; left: 0; top: 78px; width: 100%; height: 8px;
    background: linear-gradient(90deg, var(--copper), var(--copper-light) 45%, var(--copper));
  }
  .landscape {
    position: absolute; left: 0; top: 86px; width: 100%; height: 290px;
    background: linear-gradient(180deg, var(--photo-light) 0%, var(--photo-mid) 35%, var(--photo-dark) 75%, #5e5e5e 100%);
  }
  .arch { position: absolute; left: 0; top: 290px; width: 390px; height: 120px; }

  .brand { position: absolute; left: 0; top: 340px; width: 100%; text-align: center; }
  .brand__mark {
    width: 126px; height: 126px; border-radius: 50%;
    background: var(--brown); margin: 0 auto;
  }
  .brand__name {
    margin-top: 6px;
    font: 500 36px/1 "Oswald", sans-serif; letter-spacing: 1px; color: var(--brown);
  }

  .product-title {
    position: absolute; left: 0; top: 536px; width: 100%; text-align: center;
    font: 600 46px/1 "Oswald", sans-serif; letter-spacing: 2px; color: var(--brown);
  }

  .spec-panel {
    position: absolute; left: 12px; top: 607px; width: 364px; height: 222px;
    background: var(--brown-deep); color: var(--tan);
    font-family: "Oswald", sans-serif; text-align: center;
  }
  .spec-row {
    border-bottom: 1px dashed rgba(220, 192, 154, .6);
    margin: 0 6px; display: flex; align-items: center; justify-content: center;
  }
  .spec-row--variety { height: 44px; font-size: 24px; }
  .spec-row--grind { height: 36px; font-size: 17px; }
  .spec-row--notes { height: 38px; font-size: 17px; justify-content: space-between; padding: 0 14px; }
  .spec-row--roast { height: 50px; font-size: 30px; font-weight: 600; letter-spacing: 1px; }
  .spec-weight {
    height: 50px; display: flex; align-items: center; justify-content: center;
    font: 400 15px "Arimo", sans-serif; color: #fff;
  }
</style>
</head>
<body>
<main class="canvas">
  <section class="pack">
    <aside class="pack-side">
      <p class="pack-side__text">Grown on volcanic slopes, hand picked, sun dried and slow roasted for a deep, rich cup. Store sealed in a cool dry place. Brew fresh and enjoy.</p>
    </aside>

    <div class="pack-front">
      <header class="seal"><span class="seal__tagline">Premium Coffee Blend</span></header>
      <div class="copper-band"></div>

      <div class="landscape" role="img" aria-label="Black and white photograph of Mount Elgon slopes with trees and a flat-topped peak under clouds"></div>

      <svg class="arch" viewBox="0 0 390 120" aria-hidden="true">
        <defs>
          <linearGradient id="copperStroke" x1="0" x2="1">
            <stop offset="0" stop-color="#b8733a"/>
            <stop offset=".5" stop-color="#f0b46a"/>
            <stop offset="1" stop-color="#b8733a"/>
          </linearGradient>
        </defs>
        <path d="M0 80 H108 A87 87 0 0 1 282 80 H390 V120 H0 Z" fill="#e6e6e6"/>
        <path d="M0 80 H108 A87 87 0 0 1 282 80 H390" fill="none" stroke="url(#copperStroke)" stroke-width="6"/>
      </svg>

      <div class="brand">
        <div class="brand__mark"></div>
        <div class="brand__name">VELMORAQ</div>
      </div>

      <h1 class="product-title">ROASTED BEANS</h1>

      <div class="spec-panel">
        <div class="spec-row spec-row--variety">ARABICA COFFEE</div>
        <div class="spec-row spec-row--grind">100% GROUND TURKISH COFFEE</div>
        <div class="spec-row spec-row--notes"><span>FRESH ROASTED</span><span>WHOLE BEAN COFFEE</span></div>
        <div class="spec-row spec-row--roast">DARK ROAST</div>
        <div class="spec-weight">Net Wt. 1kg</div>
      </div>
    </div>
  </section>
</main>
</body>
</html>
```